Answer Choice Icons

We need four versions of an answer choice icon. We need an A, B, C and D. They need to be 40 by 40 pixels and in .png format. They will be used as the labels for the answer choices on a multiple choice test. The student will click on the A, the B, the C, or D icon to select their answer. I have uploaded an example.

Industry/Entity Type

Student

Requirements
Must have
• 40 x 40 pixels; png format
Nice to have
• An oval shape with some shine would be nice. Also having each one a different color would be good.

```html
<!DOCTYPE html>
<html lang="en">
<head>
<meta charset="utf-8">
<title>Answer Choice Icons</title>
<link href="https://fonts.googleapis.com/css2?family=Carlito:wght@400;700&display=swap" rel="stylesheet">
<style>
  :root {
    --page: #ffffff;
    --ink: #111111;
    --blue-top: #8c8fff;
    --blue: #4a4ee8;
    --blue-edge: #2d30b0;
    --amber-top: #ffd77a;
    --amber: #eaa422;
    --amber-edge: #b57a10;
    --green-top: #8fe07e;
    --green: #3fb02c;
    --green-edge: #267a18;
    --red-top: #ff8b98;
    --red: #e23a50;
    --red-edge: #a81f32;
  }
  html, body {
    margin: 0;
    padding: 0;
    width: 1200px;
    height: 900px;
    overflow: hidden;
    background: var(--page);
  }
  .canvas {
    position: relative;
    width: 1200px;
    height: 900px;
    font-family: "Carlito", "Calibri", sans-serif;
    color: var(--ink);
  }
  .question {
    position: absolute;
    left: 124px;
    top: 306px;
    margin: 0;
    font-size: 32px;
    font-weight: 400;
    letter-spacing: 0.2px;
  }
  .choices {
    position: absolute;
    left: 180px;
    top: 411px;
    margin: 0;
    padding: 0;
    list-style: none;
  }
  .choice {
    display: flex;
    align-items: center;
    height: 45px;
  }
  .choice-badge {
    position: relative;
    width: 60px;
    height: 36px;
    flex: none;
  }
  .choice-badge svg {
    position: absolute;
    inset: 0;
    width: 60px;
    height: 36px;
  }
  .choice-letter {
    position: absolute;
    inset: 0;
    display: flex;
    align-items: center;
    justify-content: center;
    font-size: 30px;
    line-height: 1;
    color: var(--ink);
    padding-top: 2px;
  }
  .choice-text {
    margin-left: 30px;
    font-size: 27px;
  }
</style>
</head>
<body>
<main class="canvas">
  <h1 class="question">Question: How much do you like this creation?</h1>

  <svg width="0" height="0" style="position:absolute">
    <defs>
      <linearGradient id="fill-blue" x1="0" y1="0" x2="0" y2="1">
        <stop offset="0" stop-color="var(--blue-top)"/><stop offset="0.55" stop-color="var(--blue)"/><stop offset="1" stop-color="var(--blue-edge)"/>
      </linearGradient>
      <linearGradient id="fill-amber" x1="0" y1="0" x2="0" y2="1">
        <stop offset="0" stop-color="var(--amber-top)"/><stop offset="0.55" stop-color="var(--amber)"/><stop offset="1" stop-color="var(--amber-edge)"/>
      </linearGradient>
      <linearGradient id="fill-green" x1="0" y1="0" x2="0" y2="1">
        <stop offset="0" stop-color="var(--green-top)"/><stop offset="0.55" stop-color="var(--green)"/><stop offset="1" stop-color="var(--green-edge)"/>
      </linearGradient>
      <linearGradient id="fill-red" x1="0" y1="0" x2="0" y2="1">
        <stop offset="0" stop-color="var(--red-top)"/><stop offset="0.55" stop-color="var(--red)"/><stop offset="1" stop-color="var(--red-edge)"/>
      </linearGradient>
      <linearGradient id="shine" x1="0" y1="0" x2="0" y2="1">
        <stop offset="0" stop-color="#fff" stop-opacity="0.75"/><stop offset="1" stop-color="#fff" stop-opacity="0.1"/>
      </linearGradient>
    </defs>
  </svg>

  <ul class="choices">
    <li class="choice">
      <span class="choice-badge">
        <svg viewBox="0 0 60 36" aria-hidden="true">
          <polygon points="1,18 12,2 48,2 59,18 48,34 12,34" fill="url(#fill-blue)" stroke="var(--blue-edge)" stroke-width="1.5"/>
          <polygon points="6,16 14,5 46,5 54,16" fill="url(#shine)"/>
        </svg>
        <span class="choice-letter">A</span>
      </span>
      <span class="choice-text">It‘s amazing!</span>
    </li>
    <li class="choice">
      <span class="choice-badge">
        <svg viewBox="0 0 60 36" aria-hidden="true">
          <polygon points="1,18 12,2 48,2 59,18 48,34 12,34" fill="url(#fill-amber)" stroke="var(--amber-edge)" stroke-width="1.5"/>
          <polygon points="6,16 14,5 46,5 54,16" fill="url(#shine)"/>
        </svg>
        <span class="choice-letter">B</span>
      </span>
      <span class="choice-text">I like it</span>
    </li>
    <li class="choice">
      <span class="choice-badge">
        <svg viewBox="0 0 60 36" aria-hidden="true">
          <polygon points="1,18 12,2 48,2 59,18 48,34 12,34" fill="url(#fill-green)" stroke="var(--green-edge)" stroke-width="1.5"/>
          <polygon points="6,16 14,5 46,5 54,16" fill="url(#shine)"/>
        </svg>
        <span class="choice-letter">C</span>
      </span>
      <span class="choice-text">It could be better</span>
    </li>
    <li class="choice">
      <span class="choice-badge">
        <svg viewBox="0 0 60 36" aria-hidden="true">
          <polygon points="1,18 12,2 48,2 59,18 48,34 12,34" fill="url(#fill-red)" stroke="var(--red-edge)" stroke-width="1.5"/>
          <polygon points="6,16 14,5 46,5 54,16" fill="url(#shine)"/>
        </svg>
        <span class="choice-letter">D</span>
      </span>
      <span class="choice-text">It‘s crap</span>
    </li>
  </ul>
</main>
</body>
</html>
```